Mortgage Protection Insurance Flyer

The target audience are new home owners so the design needs to be clean and simple.

This a primarily for Final Expense Insurance, but need an area where it says "We Also Specialize In:"
- Medicare Supplement Insurance (MediGap)
- Annuities
- Final Expense

All flyer versions need to be editable. Colors to be used are red, white or black. Refer to my website for colors and photos (harborvaleassurance.com). Will attach my logo and a flyer that I found online that is the format that I am looking for (for 8.5 in. x 11 in version). Need flyer in standard letter size 8.5 in. x11 in. but also in 8.5 in. x 5.5 in and 5.0 in. x 8.0 in. All sizes to be portrait oriented. If picked as winning design, need all flyer versions in full color, also in grey scale and files in all industry file types.

Content can be taken from my website..... harborvaleassurance.com

Do NOT submit if you are not willing to provide all versions as described above for the original project price.

Must use royalty-free stock photos please.

Target Market(s)

New homeowners looking for insurance to protect there mortgage payments

Industry/Entity Type

Life Insurance

Colors
f69fa3

Requirements
Must have
• Colors to be used are red, white or black.
• Need flyer in standard letter size 8.5 in. x11 in. but also in 3.5 in. x 8.5 in (Full Bleed 3.75 in by 8.75 in.) and 4.0 in. x 6.0 in. (Full Bleed 4.12 in x 6.12 in) Each design tailored to the size dimensions (So no squeezing 8.5 x 11 design into a 4.0 x 6.0 space.) All sizes to be portrait oriented. If picked as winning design, need all flyer versions in full color, also in grey scale and files in all file types.
• Do not need physical address on flyer, do need email address on flyer though - tkerlow@harborvaleassurance.com
• So phone number should be prominent, email address and website address should also be contact area.
• If you can not agree to terms above, do not submit any designs.
• Need facebook & twitter logos somewhere in contact info area.
Nice to have
• See sample flyers I have attached.
• White background with red used as primary graphic color and black used as secondary graphic if needed.
• font to be used should similar to one used in logo.

```html
<!DOCTYPE html>
<html lang="en">
<head>
<meta charset="utf-8">
<title>Final Expense Insurance Flyer</title>
<link rel="stylesheet" href="https://fonts.googleapis.com/css2?family=Barlow:wght@400;500;600;700;800&display=swap">
<style>
  :root {
    --red: #b3151b;
    --white: #ffffff;
    --ink: #1d1d1d;
    --grey-text: #3a3a3a;
    --backdrop: #e6e6e6;
    --photo-light: #f1ece7;
    --photo-dark: #c9b3a6;
  }
  * { box-sizing: border-box; margin: 0; padding: 0; }
  html, body { width: 1200px; height: 794px; overflow: hidden; }
  body {
    background: var(--backdrop);
    font-family: "Barlow", Arial, sans-serif;
    position: relative;
  }
  .flyer {
    position: absolute;
    left: 306px;
    top: 17px;
    width: 587px;
    height: 760px;
    background: var(--red);
    overflow: hidden;
    box-shadow: 0 4px 14px rgba(0,0,0,0.18);
  }
  .flyer-shapes { position: absolute; inset: 0; width: 587px; height: 760px; }
  .hero-photo {
    position: absolute;
    left: 300px;
    top: 44px;
    width: 262px;
    height: 228px;
    background: linear-gradient(160deg, var(--photo-light) 0%, var(--photo-dark) 100%);
    clip-path: polygon(0 0, 100% 0, 100% 96%, 0 100%);
  }
  .phone {
    position: absolute;
    left: 40px;
    top: 52px;
    color: var(--white);
    font-size: 30px;
    font-weight: 700;
    letter-spacing: 0.5px;
    line-height: 1;
  }
  .social {
    position: absolute;
    right: 34px;
    top: 20px;
    display: flex;
    gap: 6px;
  }
  .social span {
    width: 13px; height: 13px;
    border-radius: 50%;
    background: var(--white);
    display: block;
  }
  .headline {
    position: absolute;
    left: 52px;
    top: 196px;
    color: var(--ink);
    line-height: 1;
    font-size: 42px;
  }
  .headline strong { display: block; font-weight: 800; }
  .headline .light { display: block; font-weight: 400; }
  .offer {
    position: absolute;
    left: 30px;
    right: 30px;
    top: 372px;
    text-align: center;
    color: var(--white);
  }
  .offer-line {
    font-size: 18px;
    font-weight: 700;
    text-transform: uppercase;
    letter-spacing: 0.3px;
    line-height: 1.2;
    margin-bottom: 8px;
  }
  .offer-line .amount { font-size: 25px; text-transform: none; }
  .specialty-label {
    margin-top: 12px;
    font-size: 14px;
    font-weight: 700;
    letter-spacing: 0.5px;
    text-transform: uppercase;
  }
  .services {
    margin-top: 4px;
    font-size: 16px;
    font-weight: 400;
    line-height: 1.45;
  }
  .brand {
    position: absolute;
    left: 44px;
    top: 640px;
    color: var(--ink);
    font-size: 24px;
    font-weight: 800;
    letter-spacing: 1px;
    text-transform: uppercase;
    line-height: 1;
  }
  .contact {
    position: absolute;
    left: 345px;
    top: 590px;
    list-style: none;
    font-size: 12px;
    color: var(--grey-text);
  }
  .contact li { display: flex; align-items: center; gap: 8px; margin-bottom: 9px; }
  .contact li::before {
    content: "";
    width: 9px; height: 9px;
    border-radius: 50%;
    background: var(--red);
    flex: none;
  }
  .fine-print {
    position: absolute;
    left: 0; right: 0;
    top: 726px;
    text-align: center;
    color: var(--white);
    font-size: 9px;
    font-weight: 500;
  }
</style>
</head>
<body>
  <article class="flyer">
    <svg class="flyer-shapes" viewBox="0 0 587 760" aria-hidden="true">
      <path d="M0 176 C 200 150, 400 122, 587 110 L587 262 C 400 292, 200 334, 0 382 Z" fill="var(--white)"/>
      <path d="M0 612 C 200 590, 400 562, 587 540 L587 706 L0 706 Z" fill="var(--white)"/>
    </svg>

    <div class="hero-photo" role="img" aria-label="Photo of a smiling senior couple embracing, both dressed in white"></div>

    <div class="phone">(555) 014.2736</div>
    <div class="social" aria-label="Social media">
      <span></span><span></span>
    </div>

    <h1 class="headline">
      <strong>Final</strong>
      <strong>Expense</strong>
      <span class="light">Insurance</span>
    </h1>

    <section class="offer">
      <p class="offer-line">Monthly premiums as low as <span class="amount">* $10</span></p>
      <p class="offer-line">Death benefits as high as <span class="amount">$40,000</span></p>
      <p class="specialty-label">We Also Specialize In:</p>
      <p class="services">Medicare Supplement Insurance (MediGap) | Annuities<br>Final Expense | Mortgage Protection Insurance</p>
    </section>

    <div class="brand">Harborvale Assurance</div>

    <ul class="contact">
      <li>tkerlow@harborvaleassurance.com</li>
      <li>www.harborvaleassurance.com</li>
    </ul>

    <p class="fine-print">* Based on a 60 year old non-smoking female with no medical conditions and a small death benefit</p>
  </article>
</body>
</html>
```